Social Media Graphics - Bright Ridge Run REVISED

Create 6-7 individual social media graphics (square size) to encourage folks to join our online course called:

The Copper Ladder Plan
How to Launch a Multi-Million Business From Scratch
Sign Up Today!

IMPORTANT: Make the largest and most prominent text on the graphic be: How to Launch a Multi-Million Business From Scratch

For the color scheme of the graphics, let's try a blue color palette; make sure the graphics appeal to both men and women

Make sure each graphic contains 1 of the 3 pics attached (crop pic as needed); and make sure one of the graphics is all TEXT only.

Target Market(s)

men and women looking to start a business

Industry/Entity Type

Entrepreneurship

Colors
0054AA
0677BA
7BADD7
CADEEF
E8F1F8

Requirements
Must have
• All the text and use the 3 pics provided; one graphic can be all text; Simple, modern design that's easy to read

```html
<!DOCTYPE html>
<html lang="en">
<head>
<meta charset="utf-8">
<title>The Copper Ladder Plan – Social Graphic</title>
<link rel="stylesheet" href="https://fonts.googleapis.com/css2?family=Poppins:wght@700;800&family=Roboto:wght@700&display=swap">
<style>
  :root {
    --blue-deep: #0054AA;
    --blue-mid: #0677BA;
    --blue-soft: #7BADD7;
    --blue-pale: #CADEEF;
    --blue-mist: #E8F1F8;
    --shadow-navy: #0B2A55;
    --white: #FFFFFF;
  }
  * { margin: 0; padding: 0; box-sizing: border-box; }
  html, body { width: 1200px; height: 1200px; overflow: hidden; background: var(--blue-deep); }
  .graphic {
    position: relative;
    width: 1200px;
    height: 1200px;
    background: var(--blue-deep);
    overflow: hidden;
  }
  .decor { position: absolute; inset: 0; }
  .headline {
    position: absolute;
    left: 58px;
    top: 112px;
    font-family: "Poppins", sans-serif;
    font-weight: 800;
    font-size: 88px;
    line-height: 94px;
    letter-spacing: -1px;
    color: var(--blue-mist);
    text-transform: uppercase;
    text-shadow: 4px 4px 0 var(--shadow-navy);
  }
  .course-name {
    position: absolute;
    left: 58px;
    top: 680px;
    font-family: "Poppins", sans-serif;
    font-weight: 700;
    font-size: 54px;
    line-height: 74px;
    letter-spacing: 3px;
    color: var(--white);
    text-shadow: 3px 3px 0 var(--shadow-navy);
  }
  .apply-button {
    position: absolute;
    left: 58px;
    top: 897px;
    width: 368px;
    height: 70px;
    border-radius: 35px;
    background: var(--blue-mist);
    color: var(--blue-deep);
    font-family: "Roboto", sans-serif;
    font-weight: 700;
    font-size: 40px;
    display: flex;
    align-items: center;
    justify-content: center;
    letter-spacing: 0.5px;
  }
</style>
</head>
<body>
<main class="graphic">
  <svg class="decor" width="1200" height="1200" viewBox="0 0 1200 1200" aria-hidden="false">
    <defs>
      <linearGradient id="portrait-tone" x1="0" y1="0" x2="1" y2="1">
        <stop offset="0" stop-color="#C9A48A"/>
        <stop offset="0.45" stop-color="#5A4A45"/>
        <stop offset="1" stop-color="#1E2A3E"/>
      </linearGradient>
      <pattern id="dot-grid" width="51" height="51" patternUnits="userSpaceOnUse">
        <circle cx="10" cy="10" r="10" fill="#0677BA"/>
      </pattern>
    </defs>

    <!-- top-left dot grid -->
    <rect class="dots-top" x="30" y="14" width="330" height="102" fill="url(#dot-grid)"/>

    <!-- soft background circle -->
    <circle class="accent-circle" cx="1125" cy="490" r="400" fill="var(--blue-soft)"/>

    <!-- portrait frame -->
    <ellipse class="portrait-frame" cx="875" cy="690" rx="385" ry="455" fill="var(--white)"/>
    <ellipse class="portrait-photo" cx="875" cy="690" rx="368" ry="438" fill="url(#portrait-tone)"
      role="img" aria-label="Photo of the two smiling course hosts standing side by side in front of framed artwork"/>

    <!-- bottom-right dot grid -->
    <rect class="dots-bottom" x="868" y="1110" width="340" height="102" fill="url(#dot-grid)"/>
  </svg>

  <h1 class="headline">How to Launch a<br>Multi-Million<br>Business<br>From<br>Scratch</h1>

  <p class="course-name">The Copper<br>Ladder Plan</p>

  <div class="apply-button">APPLY NOW</div>
</main>
</body>
</html>
```